Ledgerwise Code Works business card design.

We are a software development company that develop Software for finance companies and related industries.

We need a 2 sided business card designed. We have a new logo already designed (see attached eps and ai) We are after a clean simple corporate look. One side with just our logo, and the second side with our details.

Glen Marwick
Managing Director

Suite 5 Level 8, 147 Hollis Parade Sydney NSW 2000

Direct: +61 2 9374 6620
Mobile: +61 4 2873 5419
Email: glenm@lcw.net.au
Web: www.lcw.net.au

I have included 2 logo files an .ai and .eps. I noticed that the lines either side of the partners looks a bit jaggered and needs to be made sharper.

I would like to introduce a little colour somewhere rather than having it all black and white. But not over the top, keeping with a simple clean corporate look. Perhaps a light blue on some of the text?

If you have other ideas would be pleased to review

Regards

Glen M.

```html
<!DOCTYPE html>
<html lang="en">
<head>
<meta charset="utf-8">
<title>Ledgerwise Code Works – Business Card</title>
<link rel="stylesheet" href="https://fonts.googleapis.com/css2?family=Lato:wght@400;700&display=swap">
<style>
  :root {
    --page-bg: #3a3a3c;
    --card-bg: #1f1f20;
    --card-edge: #2b2b2d;
    --accent: #4cc4cb;
    --text-light: #f2f2f2;
    --text-soft: #d6d6d6;
    --emboss: #3a3a3d;
    --rule: #6a6a6a;
  }
  * { box-sizing: border-box; margin: 0; padding: 0; }
  html, body {
    width: 1200px; height: 1000px; overflow: hidden;
    background: var(--page-bg);
    font-family: "Lato", Arial, sans-serif;
  }
  .canvas {
    width: 1200px; height: 1000px;
    display: flex; flex-direction: column;
    align-items: center; justify-content: center; gap: 60px;
  }
  .card {
    width: 700px; height: 400px;
    background: var(--card-bg);
    border: 1px solid var(--card-edge);
    border-radius: 18px;
    position: relative;
    overflow: hidden;
  }

  /* Details side */
  .card--details { display: flex; }
  .brand-block {
    width: 300px;
    display: flex; flex-direction: column;
    align-items: center; justify-content: center; gap: 16px;
  }
  .brand-mark {
    width: 44px; height: 44px;
    background: var(--text-light);
  }
  .brand-name {
    color: var(--text-light);
    font-weight: 700; font-size: 21px;
    letter-spacing: 0.04em; text-transform: uppercase;
    text-align: center; line-height: 1.2;
  }
  .brand-rule {
    width: 200px; height: 1px; background: var(--rule);
  }
  .details {
    flex: 1;
    padding: 56px 40px 0 20px;
    color: var(--text-light);
  }
  .person-name {
    color: var(--accent);
    font-size: 30px; font-weight: 700; line-height: 1.1;
  }
  .person-title {
    font-size: 18px; color: var(--text-soft);
    margin-top: 4px;
  }
  .contact-list {
    list-style: none; margin-top: 24px;
    display: flex; flex-direction: column; gap: 7px;
  }
  .contact-item {
    display: flex; align-items: center; gap: 12px;
    font-size: 17px; color: var(--text-light);
  }
  .contact-icon { width: 16px; height: 16px; flex: none; }
  .company-name {
    color: var(--accent);
    font-size: 18px; font-weight: 700;
    margin-top: 26px;
  }
  .address {
    font-style: normal; font-size: 17px; line-height: 1.4;
    color: var(--text-light); margin-top: 4px;
  }

  /* Logo side */
  .card--logo {
    display: flex; flex-direction: column;
    align-items: center; justify-content: center; gap: 20px;
  }
  .card--logo .brand-mark { width: 70px; height: 70px; background: var(--emboss); }
  .card--logo .brand-name { color: var(--emboss); font-size: 30px; }
  .card--logo .brand-rule { width: 300px; background: var(--emboss); }
</style>
</head>
<body>
<main class="canvas">

  <section class="card card--details" aria-label="Business card, details side">
    <div class="brand-block">
      <div class="brand-mark"></div>
      <div class="brand-name">Ledgerwise Code Works</div>
      <div class="brand-rule"></div>
    </div>
    <div class="details">
      <h1 class="person-name">Glen Marwick</h1>
      <p class="person-title">Managing Director</p>
      <ul class="contact-list">
        <li class="contact-item">
          <svg class="contact-icon" viewBox="0 0 16 16" aria-hidden="true"><path fill="#4cc4cb" d="M3.5 1.5 6 4 4.8 5.7a8 8 0 0 0 5.5 5.5L12 10l2.5 2.5-1.6 2A11 11 0 0 1 1.5 3.1z"/></svg>
          +61 2 9374 6620
        </li>
        <li class="contact-item">
          <svg class="contact-icon" viewBox="0 0 16 16" aria-hidden="true"><rect x="4" y="1" width="8" height="14" rx="1.5" fill="none" stroke="#4cc4cb" stroke-width="1.6"/><circle cx="8" cy="12.3" r="0.9" fill="#4cc4cb"/></svg>
          +61 4 2873 5419
        </li>
        <li class="contact-item">
          <svg class="contact-icon" viewBox="0 0 16 16" aria-hidden="true"><rect x="1" y="3" width="14" height="10" rx="1" fill="#4cc4cb"/><path d="M1.5 3.8 8 9l6.5-5.2" fill="none" stroke="#1f1f20" stroke-width="1.3"/></svg>
          glenm@lcw.net.au
        </li>
        <li class="contact-item">
          <svg class="contact-icon" viewBox="0 0 16 16" aria-hidden="true"><circle cx="8" cy="8" r="6.5" fill="none" stroke="#4cc4cb" stroke-width="1.5"/><path d="M1.5 8h13M8 1.5c-3 3.5-3 9.5 0 13M8 1.5c3 3.5 3 9.5 0 13" fill="none" stroke="#4cc4cb" stroke-width="1.1"/></svg>
          www.lcw.net.au
        </li>
      </ul>
      <p class="company-name">Ledgerwise Code Works</p>
      <address class="address">Suite 5 Level 8, 147<br>Hollis Parade, Sydney<br>NSW 2000</address>
    </div>
  </section>

  <section class="card card--logo" aria-label="Business card, logo side">
    <div class="brand-mark"></div>
    <div class="brand-name">Ledgerwise Code Works</div>
    <div class="brand-rule"></div>
  </section>

</main>
</body>
</html>
```